B2B flyer solution for charging infrastructures (One-Pager Din A4, double-sided)

We need a professional design for our flyer in format Din A4/both sides.
Attached you will find the content for the flyer, but we are looking for a modern, professional design.

Some background/context information:
- the product is about a solution for charging and billing of charging infrastructures (for electric cars) in companies
- target group: companies, esp. facility managers, fleet managers, controlling, CTO, CEO
- should be printed and available online
- our website (and most of our current design work): https://wendo-kraft.de

In the files you will find:
- photos of reference implementations of our solution (should be included in the flyer)
- stock photos (we are using the one you will find in the current flyer on our presentations, maybe you can use it too to keep some corporate identity.
- our logo
- the current flyer as PDF and as PowerPoint
- a sample presentation we also need for customer communication

It would be nice if the design will align with the existing design work, but bring fresh aspects and will be up-to-date and professional.

Target Market(s)

B2B, companies, fleet managers, facility managers, CTO, CIO

Industry/Entity Type

Enterprises, Charging Solutions for Electric Vehicles

Requirements
Nice to have
• Bright, light design, clean, readable

```html
<!DOCTYPE html>
<html lang="de">
<head>
<meta charset="utf-8">
<title>wendo-kraft Professional – Flyer</title>
<link href="https://fonts.googleapis.com/css2?family=Bebas+Neue&family=Montserrat:wght@400;500;600;700&display=swap" rel="stylesheet">
<style>
:root{
  --green:#76c043;
  --ink:#111;
  --paper:#fff;
  --stage:#d4d5d7;
  --night:#222;
  --sky-1:#dfe8f2;
  --sky-2:#6f93b8;
  --steel-1:#2a3c58;
  --steel-2:#101418;
}
*{box-sizing:border-box;margin:0;padding:0}
html,body{width:804px;height:1200px;overflow:hidden;background:var(--stage)}
body{position:relative;font-family:"Montserrat",sans-serif;color:var(--ink)}
.flyer{position:absolute;left:71px;width:663px;height:468px;background:var(--paper);overflow:hidden}
.flyer--front{top:65px}
.flyer--back{top:630px}
.abs{position:absolute}
.headline{font-family:"Bebas Neue",sans-serif;line-height:1;white-space:nowrap;letter-spacing:.2px}
.headline .accent{color:var(--green)}
.wordmark{font-weight:500;white-space:nowrap}

/* front */
.front-logo{left:20px;top:66px;font-size:21px}
.front-logo-dot{left:20px;top:40px;width:18px;height:18px;border-radius:50%;background:var(--green)}
.front-headline{left:15px;top:128px;font-size:37px}
.front-sub{left:15px;top:163px;font-size:10.3px;font-weight:700;line-height:1.2}
.section-title{color:var(--green);font-weight:700;font-size:14px}
.leistungen-title{left:15px;top:208px}
.profit-title{left:15px;top:348px;font-size:14.5px}
.bullet-list{list-style:none;font-size:10.2px;line-height:12.3px}
.bullet-list li{position:relative;padding-left:20px;margin-bottom:3px}
.bullet-list li::before{content:"";position:absolute;left:2px;top:3px;width:7px;height:7px;border-radius:50%;background:var(--green)}
.leistungen-list{left:15px;top:236px;width:330px}
.profit-list{left:15px;top:375px;width:290px}
.profit-list li{margin-bottom:4px}
.contact{right:20px;top:334px;text-align:right;color:#fff;font-size:9.9px;line-height:11.8px}
.contact .section-title{font-size:13.5px;line-height:16px}
.contact .cta{margin-top:9px}

/* back */
.back-tab{left:0;top:0;width:284px;height:60px;background:var(--green);border-bottom-right-radius:60px 60px}
.back-logo{left:20px;top:16px;font-size:21px;color:#fff}
.back-logo-dot{left:-999px}
.back-headline{left:15px;top:68px;font-size:50px}
.pill{left:15px;top:122px;height:16px;padding:0 7px;border-radius:8px;background:var(--green);color:#fff;font-size:10.5px;font-weight:600;line-height:16px;white-space:nowrap}
.audience{left:16px;width:56px;text-align:center;font-size:6.8px;font-weight:700;line-height:7.4px}
.audience .icon-box{width:44px;height:43px;margin:0 auto 6px;border:1px solid #cfe7bd;border-radius:4px;display:flex;align-items:center;justify-content:center;box-shadow:0 1px 2px rgba(0,0,0,.12)}
.divider{left:75px;top:150px;width:1px;height:303px;background:#d8ecc9}
.features{left:86px;top:158px;width:330px}
.features h2{font-family:"Bebas Neue",sans-serif;font-weight:400;font-size:23px;line-height:1;white-space:nowrap;margin-bottom:6px}
.features h3{color:var(--green);font-size:13.5px;font-weight:700;line-height:16.5px;margin-bottom:4px}
.features p,.features li{font-size:9.8px;line-height:11.4px}
.features ul{list-style:none;margin-bottom:6px}
.features li{padding-left:6px;text-indent:-6px}
.features li::before{content:"· "}
</style>
</head>
<body>

<section class="flyer flyer--front">
  <svg class="abs" style="left:0;top:0" width="663" height="468" viewBox="0 0 663 468">
    <defs>
      <linearGradient id="sky" x1="0" y1="0" x2="1" y2="1">
        <stop offset="0" stop-color="#c9d9ea"/><stop offset=".5" stop-color="var(--sky-1)"/><stop offset="1" stop-color="var(--sky-2)"/>
      </linearGradient>
      <linearGradient id="garage" x1="0" y1="0" x2="1" y2="1">
        <stop offset="0" stop-color="#3a3a3a"/><stop offset="1" stop-color="#1b1b1b"/>
      </linearGradient>
      <linearGradient id="wallbox" x1="0" y1="0" x2="1" y2="0">
        <stop offset="0" stop-color="#eceeef"/><stop offset="1" stop-color="#9a9fa3"/>
      </linearGradient>
    </defs>
    <path d="M4 108 C120 110 190 95 210 43" fill="none" stroke="var(--green)" stroke-width="1.3"/>
    <path d="M418 468 L418 330 C450 290 500 265 540 265 L663 265 L663 468 Z" fill="url(#garage)" role="img" aria-label="Photo: electric car parked in a dark garage"/>
    <path d="M329 0 C340 170 470 305 663 290 L663 0 Z" fill="var(--green)"/>
    <path d="M329 0 C342 158 470 290 663 276 L663 0 Z" fill="url(#sky)" role="img" aria-label="Photo: charging plug inserted into an electric car"/>
    <rect x="342" y="304" width="70" height="164" rx="6" fill="url(#wallbox)" role="img" aria-label="Photo: wall-mounted charging station with green cable"/>
  </svg>

  <div class="abs front-logo-dot"></div>
  <div class="abs wordmark front-logo">wendo-kraft.de</div>

  <h1 class="abs headline front-headline"><span class="accent">WENDO-KRAFT</span> PROFESSIONAL</h1>
  <p class="abs front-sub">die maßgeschneiderte B2B-Abrechnungslösung<br>für Elektromobilität</p>

  <h2 class="abs section-title leistungen-title">Leistungen:</h2>
  <ul class="abs bullet-list leistungen-list">
    <li>Vielseitige Abrechnungsmöglichkeiten für Fuhrpark, Mitarbeiter, Partnerunternehmen, Mieter, Kunden und andere.</li>
    <li>Full-Service-Betreuung (Monitoring, Abrechnung, Benutzerbetreuung)</li>
    <li>Integration in ihre Unternehmensabläufe</li>
    <li style="white-space:nowrap">Berücksichtigung von Eigentümer/Mieter-Konstellationen</li>
  </ul>

  <h2 class="abs section-title profit-title">Mit wendo-kraft Professional profitieren:</h2>
  <ul class="abs bullet-list profit-list">
    <li>· Effizienter Verwaltung von Lade-Infrastruktur</li>
    <li>· Umfassende Full-Service-Betreuung</li>
    <li>· Nahtloser Integration in Ihre kaufmännischen Prozesse</li>
    <li>· Vielseitigen Abrechnungsmöglichkeiten</li>
  </ul>

  <div class="abs contact">
    <div class="section-title">Kontaktieren Sie uns</div>
    <p>Erfahren Sie mehr über wendo-kraft<br>und wie wir Ihre Abrechnungsanforderungen<br>erfüllen können.</p>
    <div class="section-title cta">für eine kostenlose Beratung:</div>
    <p>Telefon: +49 (0) 30 555 0142<br>E-Mail: info@wendo-kraft.de<br>Web: www.wendo-kraft.de</p>
  </div>
</section>

<section class="flyer flyer--back">
  <svg class="abs" style="left:0;top:0" width="663" height="468" viewBox="0 0 663 468">
    <defs>
      <linearGradient id="solar" x1="1" y1="0" x2="0" y2="1">
        <stop offset="0" stop-color="var(--steel-1)"/><stop offset=".55" stop-color="#3f5f86"/><stop offset="1" stop-color="var(--steel-2)"/>
      </linearGradient>
    </defs>
    <path d="M410 468 C410 230 520 70 620 0 L663 0 L663 468 Z" fill="var(--green)"/>
    <path d="M418 468 C418 240 525 80 663 5 L663 468 Z" fill="url(#solar)" role="img" aria-label="Photo: charging plug under a solar panel carport"/>
  </svg>

  <div class="abs back-tab"></div>
  <div class="abs wordmark back-logo">wendo-kraft.de</div>

  <h1 class="abs headline back-headline"><span class="accent">WENDO-KRAFT</span> PROFESSIONAL</h1>
  <div class="abs pill">die Funktionen im Überblick</div>

  <div class="abs audience" style="top:152px">
    <div class="icon-box"><svg width="32" height="14" viewBox="0 0 32 14"><path d="M2 10 L4 5 Q5 3 8 3 L16 3 Q19 3 21 5 L24 7 L29 8 Q31 9 31 11 L31 12 L1 12 L1 11 Z" fill="#333"/><circle cx="8" cy="12" r="2" fill="#333"/><circle cx="24" cy="12" r="2" fill="#333"/></svg></div>
    Fuhrpark,<br>Dienstwagen
  </div>
  <div class="abs audience" style="top:227px">
    <div class="icon-box"><svg width="30" height="20" viewBox="0 0 30 20"><circle cx="7" cy="5" r="3.5" fill="#111"/><circle cx="23" cy="5" r="3.5" fill="#111"/><circle cx="15" cy="8" r="4" fill="#111"/><path d="M1 15 Q7 8 13 14 Z M17 14 Q23 8 29 15 Z M7 20 Q15 9 23 20 Z" fill="#111"/></svg></div>
    Mitarbeiter<br>Privatfahrzeuge
  </div>
  <div class="abs audience" style="top:302px">
    <div class="icon-box"><svg width="26" height="28" viewBox="0 0 26 28"><g fill="#111"><circle cx="6" cy="4" r="2.5"/><circle cx="13" cy="4" r="2.5"/><circle cx="20" cy="4" r="2.5"/><circle cx="6" cy="13" r="2.5"/><circle cx="13" cy="13" r="2.5"/><circle cx="20" cy="13" r="2.5"/><rect x="2" y="16" width="22" height="9" rx="3"/><rect x="2" y="7" width="22" height="4" rx="2"/></g></svg></div>
    Kunden und<br>Gäste
  </div>
  <div class="abs audience" style="top:377px">
    <div class="icon-box"><svg width="28" height="24" viewBox="0 0 28 24"><g fill="#111"><rect x="8" y="0" width="8" height="24"/><rect x="1" y="9" width="6" height="15"/><rect x="18" y="5" width="9" height="19"/></g><g fill="#fff"><rect x="10" y="3" width="1.5" height="2"/><rect x="13" y="3" width="1.5" height="2"/><rect x="20" y="8" width="1.5" height="2"/><rect x="23" y="8" width="1.5" height="2"/><rect x="3" y="12" width="1.5" height="2"/></g></svg></div>
    Vermieter,<br>Eigentümer
  </div>
  <div class="abs divider"></div>

  <div class="abs features">
    <h2>VERRECHNUNG VON LADEVORGÄNGEN FÜR:</h2>
    <h3>Full-Service-Betreuung für<br>sorgenfreies Management</h3>
    <p>wendo-kraft übernimmt auf Wunsch alle organisatorischen<br>Belange bei der Verwaltung Ihrer Lade-Infrastruktur, einschließlich:</p>
    <ul>
      <li>Monitoring</li>
      <li>Support</li>
      <li>User-Onboarding und -Support</li>
      <li>Handling von Zugangskarten</li>
      <li>Integration von firmeninternen Zugangstoken</li>
    </ul>
    <h3>Perfekte Integration in<br>kaufmännische Prozesse</h3>
    <p>wendo-kraft fügt sich nahtlos in die kaufmännischen Strukturen<br>moderner Unternehmen ein und bietet:</p>
    <ul>
      <li>Erweitertes Reporting</li>
      <li>Aufschlüsselung und Tarifierung nach Nutzergruppe</li>
      <li>Unterstützung unternehmensinterner Abrechnung und Verrechnung und/oder Zahlungseinzug durch wendo-kraft</li>
      <li>Schnittstellen zu Buchhaltung und Lohnbuchhaltung</li>
      <li>Bedarfsgerechte Anpassbarkeit</li>
    </ul>
  </div>
</section>

</body>
</html>
```